Orthopedic Arm Surgeon Brochure

Bifold modern design. I will supply the text, my photo, and photos of my textbooks. Prefer colors in the greens, blues, greys. For more information visit LimbForwardClinic.com Please feel free to e-mail me with any questions. Current brochure attached; I want to modernize this, get rid of frames, and change the text.

Target Market(s)

High-end market

Colors
3176b5
33a6d7
33b8a4
abd036
876aae
b768aa

Requirements
Must have
• Beautiful finishes
Should not have
• Bright reds, yellows, oranges that emit fear

```html
<!DOCTYPE html>
<html lang="en">
<head>
<meta charset="utf-8">
<title>Daniel R. Hartwell, MD – Brochure Panel</title>
<link href="https://fonts.googleapis.com/css2?family=PT+Serif:wght@400;700&display=swap" rel="stylesheet">
<style>
  :root{
    --backdrop:#dcdcdc;
    --paper:#fbfbfb;
    --ink:#141414;
    --teal:#33b0a0;
    --cover-tan:#b99a5c;
    --cover-blue:#2f6fc0;
    --cover-red:#9e1b22;
    --cover-purple:#4a2f6e;
    --cover-brown:#5a3318;
    --cover-sky:#c9d6e6;
    --cover-navy:#2a2250;
    --photo-dark:#2a2a2e;
    --photo-light:#d9d4cf;
  }
  *{margin:0;padding:0;box-sizing:border-box}
  html,body{width:1200px;height:1200px;overflow:hidden}
  body{background:var(--backdrop);font-family:"PT Serif",Georgia,serif;color:var(--ink)}
  .panel{position:absolute;left:200px;top:60px;width:800px;height:1080px;background:var(--paper);
    box-shadow:0 6px 24px rgba(0,0,0,.12);overflow:hidden}
  .portrait{position:absolute;left:120px;top:110px;width:350px;height:340px;
    background:linear-gradient(160deg,var(--photo-light) 0%,#8d8a88 35%,var(--photo-dark) 70%);z-index:2}
  .profile{position:absolute;left:500px;top:100px;width:270px}
  .profile h1{font-size:38px;line-height:1.05;font-weight:700;letter-spacing:-.4px}
  .profile .rule{width:34px;height:5px;background:var(--ink);margin:18px 0 14px}
  .profile p{font-size:16px;line-height:1.3}
  .book-band{position:absolute;left:0;top:440px;width:800px;height:170px;background:var(--teal);
    display:flex;gap:14px;align-items:center;padding:0 31px}
  .book{width:80px;height:135px;flex:none}
  .book.tan{background:linear-gradient(135deg,#d9c38b,var(--cover-tan))}
  .book.blue{background:linear-gradient(135deg,#4d8fe0,var(--cover-blue))}
  .book.red{background:linear-gradient(135deg,#c0303a,var(--cover-red))}
  .book.purple{background:linear-gradient(135deg,#6a4a96,var(--cover-purple))}
  .book.brown{background:linear-gradient(180deg,var(--cover-sky) 0 40%,var(--cover-brown) 40%)}
  .book.sky{background:linear-gradient(160deg,#ffffff,#9fb4cf 60%,#2e4f8a)}
  .book.navy{background:linear-gradient(90deg,#b8742c 0 22%,var(--cover-navy) 22%)}
  .book.slate{background:linear-gradient(135deg,#4b5f7a,#25324a)}
  .locations{position:absolute;left:60px;top:645px;width:700px;height:400px}
  .locations h2{font-size:22px;font-weight:700;line-height:1.25;width:460px}
  .site{font-size:19px;line-height:1.3;position:absolute;white-space:nowrap}
  .site strong{display:block;font-size:20px}
  .site.central{left:0;top:80px}
  .site.north{left:0;top:175px}
  .site.south{left:360px;top:215px}
  .site.west{left:360px;top:305px}
  .web{position:absolute;left:60px;top:985px;font-size:19px}
</style>
</head>
<body>
  <main class="panel">
    <div class="portrait" role="img" aria-label="Portrait photograph of the surgeon in a dark suit"></div>

    <section class="profile">
      <h1>Daniel R. Hartwell, MD</h1>
      <div class="rule"></div>
      <p>Dr. Hartwell is Nationally-recognized Upper Extremity Surgeon who has edited 7 textbook, published over 45 original research papers and written 23 textbook chapters</p>
    </section>

    <div class="book-band">
      <div class="book tan" role="img" aria-label="Textbook cover"></div>
      <div class="book blue" role="img" aria-label="Textbook cover"></div>
      <div class="book red" role="img" aria-label="Textbook cover"></div>
      <div class="book purple" role="img" aria-label="Textbook cover"></div>
      <div class="book brown" role="img" aria-label="Textbook cover"></div>
      <div class="book sky" role="img" aria-label="Textbook cover with athlete photo"></div>
      <div class="book navy" role="img" aria-label="Textbook cover with athlete photo"></div>
      <div class="book slate" role="img" aria-label="Textbook cover"></div>
    </div>

    <section class="locations">
      <h2>Dr Hartwell sees patients at the following location :</h2>
      <div class="site central"><strong>Bayou Medical Plaza</strong>4410 Linden Street Suite 1016<br>Riverton, Texas 77031</div>
      <div class="site north"><strong>Cedar Hollow</strong>8820 County Road 12 West<br>Riverton, Texas 77068</div>
      <div class="site south"><strong>Maplewood</strong>2750 Lakeview Health Dr<br>Suite 202 Maplewood, Texas 77589</div>
      <div class="site west"><strong>Elmstead</strong>315 Orchard Grove Dr. Elmstead, Texas<br>77452</div>
    </section>

    <div class="web">www.LimbForwardClinic.com</div>
  </main>
</body>
</html>
```